Visual consulting framework

Thornwell Advisory is a financial consulting business that takes it clients on the following journey:
1. Get fit (disciplined)
2. Get funded (access to capital)
3. Get big (grow)
4. Get out (exit with wealth)
Over thirty years we have identified that the key to being successful on this journey are the following elements or components.
1. Vision
2. Strategy
3. Structure
4. Product & services
5. Sales and marketing
6. System and processes
7. People
8. Culture
9. Finance
10. M&A
11. Performance monitoring
12. Risk management
We require a visual representation of these elements and the journey to communicate to clients and prospects in marketing material.
Look and feel
Each slider illustrates characteristics of the customer's brand and the style your logo design should communicate.

```html
<!DOCTYPE html>
<html lang="en">
<head>
<meta charset="utf-8">
<title>Thornwell Advisory – Consulting Framework</title>
<link href="https://fonts.googleapis.com/css2?family=Poppins:wght@300;400;500;700;800&display=swap" rel="stylesheet">
<style>
  :root {
    --ink: #0b0b0b;
    --brand-orange: #f28c1e;
    --brand-blue: #0ea5e4;
    --badge-ink: #5a5a5a;
    --strategy: #f22c00;
    --structure: #d70000;
    --product: #ad0069;
    --sales: #f9e41f;
    --systems: #fcc62a;
    --people: #f97306;
    --culture: #4b1063;
    --finance: #5f3a8e;
    --mna: #0000d6;
    --performance: #007f7a;
    --risk: #218a22;
    --vision: #a9d110;
    --stage-fit: #e0062a;
    --stage-funded: #fdb813;
    --stage-big: #3a1fb5;
    --stage-out: #25993c;
    --leader-orange: #f5891f;
    --leader-blue: #16a6e2;
  }
  * { margin: 0; padding: 0; box-sizing: border-box; }
  html, body { width: 856px; height: 1200px; overflow: hidden; background: #fff; }
  .page { position: relative; width: 856px; height: 1200px; font-family: "Poppins", sans-serif; }
  .brand {
    position: absolute; top: 92px; left: 0; width: 856px;
    display: flex; justify-content: center; align-items: center; gap: 14px;
  }
  .brand-dot { width: 34px; height: 34px; border-radius: 50%; background: var(--brand-blue); }
  .brand-name { font-size: 32px; font-weight: 500; color: var(--brand-orange); letter-spacing: 0.5px; }
  .purpose {
    position: absolute; top: 256px; left: 0; width: 856px; text-align: center;
    font-size: 25px; font-weight: 800; line-height: 33px; color: var(--ink); letter-spacing: -0.2px;
  }
  .wheel { position: absolute; left: 0; top: 380px; width: 856px; height: 760px; }
  .petal-label { font-family: "Poppins", sans-serif; font-weight: 700; font-size: 11.5px; fill: #fff; text-anchor: middle; }
  .badge-number { font-family: "Poppins", sans-serif; font-weight: 800; font-size: 18px; fill: var(--badge-ink); text-anchor: middle; }
  .stage-label { font-family: "Poppins", sans-serif; font-weight: 700; font-size: 12px; fill: #fff; letter-spacing: 4px; }
  .leader-top { font-family: "Poppins", sans-serif; font-weight: 800; font-size: 31px; fill: var(--leader-orange); text-anchor: middle; }
  .leader-bottom { font-family: "Poppins", sans-serif; font-weight: 300; font-size: 31px; fill: var(--leader-blue); text-anchor: middle; letter-spacing: 3px; }
</style>
</head>
<body>
<div class="page">
  <header class="brand">
    <span class="brand-dot"></span>
    <span class="brand-name">Thornwell Advisory</span>
  </header>

  <h1 class="purpose">OUR PURPOSE IS CLEAR, WE GET COMPANIES<br>AND THEIR FOUNDERS, FIT, FUNDED, BIG AND OUT</h1>

  <svg class="wheel" viewBox="-425 -363 856 760" aria-label="Twelve framework elements around the market leader journey">
    <defs>
      <filter id="soft-shadow" x="-30%" y="-30%" width="160%" height="160%">
        <feDropShadow dx="0" dy="2" stdDeviation="3" flood-opacity="0.25"/>
      </filter>
      <path id="petal" d="M0 0 L280 -94 C338 -112 362 -62 360 0 C358 62 338 112 280 94 Z"/>
      <path id="arc-fit" d="M-70.7 -70.7 A100 100 0 0 1 70.7 -70.7"/>
      <path id="arc-funded" d="M70.7 -70.7 A100 100 0 0 1 70.7 70.7"/>
      <path id="arc-out" d="M-70.7 70.7 A100 100 0 0 1 -70.7 -70.7"/>
      <path id="arc-big" d="M-76.4 76.4 A108 108 0 0 0 76.4 76.4"/>
    </defs>

    <g class="petals" filter="url(#soft-shadow)">
      <use href="#petal" fill="var(--finance)" transform="rotate(90)"/>
      <use href="#petal" fill="var(--culture)" transform="rotate(60)"/>
      <use href="#petal" fill="var(--people)" transform="rotate(30)"/>
      <use href="#petal" fill="var(--systems)" transform="rotate(0)"/>
      <use href="#petal" fill="var(--sales)" transform="rotate(-30)"/>
      <use href="#petal" fill="var(--product)" transform="rotate(-60)"/>
      <use href="#petal" fill="var(--structure)" transform="rotate(-90)"/>
      <use href="#petal" fill="var(--strategy)" transform="rotate(-120)"/>
      <use href="#petal" fill="var(--vision)" transform="rotate(-150)"/>
      <use href="#petal" fill="var(--risk)" transform="rotate(180)"/>
      <use href="#petal" fill="var(--performance)" transform="rotate(150)"/>
      <use href="#petal" fill="var(--mna)" transform="rotate(120)"/>
    </g>

    <circle class="inner-shade" r="200" fill="rgba(0,0,0,0.12)"/>

    <g class="label-discs" fill="rgba(0,0,0,0.13)">
      <circle cx="-132" cy="-229" r="54"/>
      <circle cx="0" cy="-264" r="54"/>
      <circle cx="132" cy="-229" r="54"/>
      <circle cx="229" cy="-132" r="54"/>
      <circle cx="264" cy="0" r="54"/>
      <circle cx="229" cy="132" r="54"/>
      <circle cx="132" cy="229" r="54"/>
      <circle cx="0" cy="264" r="54"/>
      <circle cx="-132" cy="229" r="54"/>
      <circle cx="-229" cy="132" r="54"/>
      <circle cx="-264" cy="0" r="54"/>
      <circle cx="-229" cy="-132" r="54"/>
    </g>

    <g class="petal-labels">
      <text class="petal-label" x="-132" y="-225">STRATEGY</text>
      <text class="petal-label" x="0" y="-260">STRUCTURE</text>
      <text class="petal-label" x="132" y="-240"><tspan x="132">PRODUCT</tspan><tspan x="132" dy="12">&amp;</tspan><tspan x="132" dy="12">SERVICES</tspan></text>
      <text class="petal-label" x="229" y="-143"><tspan x="229">SALES</tspan><tspan x="229" dy="12">&amp;</tspan><tspan x="229" dy="12">MARKETING</tspan></text>
      <text class="petal-label" x="264" y="-11"><tspan x="264">SYSTEM</tspan><tspan x="264" dy="12">&amp;</tspan><tspan x="264" dy="12">PROCESSES</tspan></text>
      <text class="petal-label" x="229" y="136">PEOPLE</text>
      <text class="petal-label" x="132" y="233">CULTURE</text>
      <text class="petal-label" x="0" y="268">FINANCE</text>
      <text class="petal-label" x="-132" y="233">M &amp; A</text>
      <text class="petal-label" x="-229" y="126"><tspan x="-229">PERFORMANCE</tspan><tspan x="-229" dy="19">MONITORING</tspan></text>
      <text class="petal-label" x="-264" y="-6"><tspan x="-264">RISK</tspan><tspan x="-264" dy="19">MANAGEMENT</tspan></text>
      <text class="petal-label" x="-229" y="-128">VISION</text>
    </g>

    <g class="petal-icons" fill="rgba(255,255,255,0.22)">
      <circle cx="-75" cy="-130" r="21" role="img" aria-label="Strategy icon: light bulb with target"/>
      <circle cx="0" cy="-150" r="21" role="img" aria-label="Structure icon: organisation chart"/>
      <circle cx="75" cy="-130" r="21" role="img" aria-label="Product and services icon: parcels"/>
      <circle cx="130" cy="-75" r="21" role="img" aria-label="Sales and marketing icon: megaphone"/>
      <circle cx="150" cy="0" r="21" role="img" aria-label="Systems and processes icon: gears"/>
      <circle cx="130" cy="75" r="21" role="img" aria-label="People icon: group of people"/>
      <circle cx="75" cy="130" r="21" role="img" aria-label="Culture icon: hands around a globe"/>
      <circle cx="0" cy="150" r="21" role="img" aria-label="Finance icon: calculator and invoice"/>
      <circle cx="-75" cy="130" r="21" role="img" aria-label="M and A icon: handshake"/>
      <circle cx="-130" cy="75" r="21" role="img" aria-label="Performance monitoring icon: dashboard"/>
      <circle cx="-150" cy="0" r="21" role="img" aria-label="Risk management icon: chart with warning"/>
      <circle cx="-130" cy="-75" r="21" role="img" aria-label="Vision icon: eye in target"/>
    </g>

    <g class="journey-hub">
      <circle r="121" fill="#fff" filter="url(#soft-shadow)"/>
      <g fill="none" stroke-width="22">
        <path d="M-73.5 -73.5 A104 104 0 0 1 73.5 -73.5" stroke="var(--stage-fit)"/>
        <path d="M73.5 -73.5 A104 104 0 0 1 73.5 73.5" stroke="var(--stage-funded)"/>
        <path d="M73.5 73.5 A104 104 0 0 1 -73.5 73.5" stroke="var(--stage-big)"/>
        <path d="M-73.5 73.5 A104 104 0 0 1 -73.5 -73.5" stroke="var(--stage-out)"/>
      </g>
      <circle r="90" fill="#fff"/>
      <text class="stage-label" text-anchor="middle"><textPath href="#arc-fit" startOffset="50%">GET FIT</textPath></text>
      <text class="stage-label" text-anchor="middle"><textPath href="#arc-funded" startOffset="50%">GET FUNDED</textPath></text>
      <text class="stage-label" text-anchor="middle"><textPath href="#arc-out" startOffset="50%">GET OUT</textPath></text>
      <text class="stage-label" text-anchor="middle"><textPath href="#arc-big" startOffset="50%">GET BIG</textPath></text>
      <text class="leader-top" x="0" y="-2">MARKET</text>
      <text class="leader-bottom" x="0" y="31">LEADER</text>
    </g>

    <g class="badges">
      <g filter="url(#soft-shadow)" fill="#fff">
        <circle cx="-210" cy="-253" r="20"/>
        <circle cx="-56" cy="-325" r="20"/>
        <circle cx="113" cy="-309" r="20"/>
        <circle cx="252" cy="-212" r="20"/>
        <circle cx="322" cy="-56" r="20"/>
        <circle cx="306" cy="113" r="20"/>
        <circle cx="209" cy="251" r="20"/>
        <circle cx="55" cy="322" r="20"/>
        <circle cx="-115" cy="306" r="20"/>
        <circle cx="-253" cy="208" r="20"/>
        <circle cx="-325" cy="54" r="20"/>
        <circle cx="-309" cy="-115" r="20"/>
      </g>
      <text class="badge-number" x="-210" y="-247">01</text>
      <text class="badge-number" x="-56" y="-319">02</text>
      <text class="badge-number" x="113" y="-303">03</text>
      <text class="badge-number" x="252" y="-206">04</text>
      <text class="badge-number" x="322" y="-50">05</text>
      <text class="badge-number" x="306" y="119">06</text>
      <text class="badge-number" x="209" y="257">07</text>
      <text class="badge-number" x="55" y="328">08</text>
      <text class="badge-number" x="-115" y="312">09</text>
      <text class="badge-number" x="-253" y="214">10</text>
      <text class="badge-number" x="-325" y="60">11</text>
      <text class="badge-number" x="-309" y="-109">12</text>
    </g>
  </svg>
</div>
</body>
</html>
```